MODERN + COOL Business Card Needed!

SUMMARY
This is for a 40+ year old family business that is transitioning to the 2nd generation and is in real need of a more modern facelift. Ive attached a company logo (I made quickly as an idea with my limited PSD skills) to start off with that you are welcome to change and draw ideas from. Ive also attached some screen shots of cards I like to give you an idea of my preferences.

WHAT WE DO
The company name is Tall Pine HK Ltd. But I prefer to just call it Tall Pine or Tall Pine with Hong Kong as kind of a sub heading on the business card. We own a factory as well as help our customers find factories to make their product. Product I mean, toys 99.9% of the time. Simple old school toys like board games, puzzles, wooden toys, baby/infant toys.

You can say we are a "sourcing" or "trading" or "consulting" company with a factory to help you do it. But since we deal with toys, i like to keep it modern and cool and fun, not serious like managing hedge funds.

WHAT WE ARE LOOKING FOR
A cool, unique looking business card that stands out. In terms of design, something modern and professional. I like darker colored cards and I like colors such as blue/green/dark gray, but am open to other colored themes. I Like bright lime green with gray, always though thats a nice combo. I prefer cards that are all colored and not so much white showing (I think). Ive attached a few screenshots of cards so take a look to get a feel of what I like.

We do alot of wooden stacking games in variety of colors too like Tovra, Lumo, Towerplix (google these to check them out). So designs that sort of resemble stacking or building would be cool but totally not necessary.

In terms of the physical aspects of the card, Im looking for a card a bit different than the standard rectangular shape. Double sided. Little things like having corner(s) be round or different angle instead of square edge I always thought was nice. Its got to be mostly a normal card size, no folding or smaller cards that fit weird in your wallet. No vertical designs. Am open to VERY different/creative shapes (as long as it still fits in a wallet good like a normal buisness card.
Updates

Hi everyone!

Just wanted to write a message to everyone to let them know all submissions are being reviewed or have been reviewed.  If I have not responded with feedback, rest assure your submission was definitely looked at in detail but I either have just been too busy to respond (alot of submissions!), or its on my to be considered list.

I respect and really enjoy receiving everyones creativity and work so I dont want it to go unrecognized - thus this message!  Feel free to submit more ideas if you like until this project ends.  Sometimes some designs just dont click but sometimes they can so you never know!

Thanks again for everyones participation and great work!

~Dev Orr

Target Market(s)

The cards are mainly handed to toy company sourcers and buyers. People I talk to ... say Pelvane for example... might want to make their next edition of Farthingale game with a reputable factory at a good cost so they can sell it to stores at a profit.

So these are the types of people I often try to talk and introduce myself and my company to.

Industry/Entity Type

Building

Colors
acd036
0392cd
00a88e
474747
606060

Requirements
Must have
• Just double sided, not plain rectangle corners, and just cool to look at and catches your eye!

Oh and the obvious business card stuff like place for name, address, number, email, etc.
Nice to have
• Think more modern and fun, not serious and old fashion (thats what we used to be!). Can use the logo I attached and you can definitely alter and change the logo or make a whole new one!

Oh and can definitely use a creative slogan if you like to think of one based on what I described in what we do.
Should not have
• Dont use fonts or text placement that might make "Tall Pine" look like "Tal Lpine"... We arent selling news papers!!

Please nothing related to education since we have the word Pine in the title, thats not our business at all.

Logo and design should not be too heavy on things related to toys, as though thats what we primarily focus on now, what we do may change over time.

```html
<!DOCTYPE html>
<html lang="en">
<head>
<meta charset="utf-8">
<title>Tall Pine – Business Card</title>
<link rel="stylesheet" href="https://fonts.googleapis.com/css2?family=Fredoka:wght@600&display=swap">
<style>
  :root {
    --page-bg: #ffffff;
    --card-bg: #050707;
    --brand-teal: #2b9aa8;
    --tile-magenta: #e0196e;
    --tile-lime: #acd036;
    --tile-blue: #1592d2;
    --tile-orange: #f4702c;
    --tile-yellow: #ece42a;
    --tile-green: #14a88e;
    --tile-gray: #606060;
    --tile-navy: #2b2a6a;
  }
  * { margin: 0; padding: 0; box-sizing: border-box; }
  html, body {
    width: 1200px;
    height: 471px;
    overflow: hidden;
    background: var(--page-bg);
  }
  .sheet {
    position: relative;
    width: 1200px;
    height: 471px;
  }
  .card {
    position: absolute;
    top: 39px;
    width: 581px;
    height: 387px;
    border-radius: 29px;
    background: var(--card-bg);
    overflow: hidden;
  }
  .card--front { left: 0; }
  .card--back { left: 619px; }
  .tile-mark {
    position: absolute;
    display: block;
  }
  .card--front .tile-mark {
    left: 3px;
    top: 0;
    width: 388px;
    height: 387px;
  }
  .card--back .tile-mark {
    left: -192px;
    top: 0;
    width: 432px;
    height: 391px;
  }
  .brand-name {
    position: absolute;
    left: 376px;
    top: 163px;
    width: 190px;
    font-family: "Fredoka", sans-serif;
    font-weight: 600;
    font-size: 68px;
    line-height: 74px;
    letter-spacing: 2px;
    color: var(--brand-teal);
    text-align: center;
    text-transform: uppercase;
  }
  .contact-list {
    position: absolute;
    left: 262px;
    top: 132px;
    list-style: none;
    font-family: "Fredoka", sans-serif;
    font-weight: 600;
    font-size: 22px;
    line-height: 34px;
    color: var(--brand-teal);
  }
</style>
</head>
<body>
<main class="sheet">
  <section class="card card--front" aria-label="Card front">
    <svg class="tile-mark" viewBox="0 0 388 387" role="img" aria-label="Diamond mosaic of bright coloured triangles">
      <defs>
        <linearGradient id="tile-blend-front" x1="0" y1="0" x2="1" y2="1">
          <stop offset="0" stop-color="var(--tile-lime)"/>
          <stop offset="0.3" stop-color="var(--tile-magenta)"/>
          <stop offset="0.5" stop-color="var(--tile-yellow)"/>
          <stop offset="0.7" stop-color="var(--tile-orange)"/>
          <stop offset="1" stop-color="var(--tile-green)"/>
        </linearGradient>
      </defs>
      <polygon points="194,0 388,193 194,387 0,193" fill="url(#tile-blend-front)"/>
    </svg>
    <h1 class="brand-name">Tall<br>Pine</h1>
  </section>

  <section class="card card--back" aria-label="Card back">
    <svg class="tile-mark" viewBox="0 0 432 391" role="img" aria-label="Half of the diamond mosaic of bright coloured triangles">
      <defs>
        <linearGradient id="tile-blend-back" x1="0" y1="0" x2="1" y2="1">
          <stop offset="0" stop-color="var(--tile-blue)"/>
          <stop offset="0.35" stop-color="var(--tile-magenta)"/>
          <stop offset="0.55" stop-color="var(--tile-yellow)"/>
          <stop offset="0.75" stop-color="var(--tile-orange)"/>
          <stop offset="1" stop-color="var(--tile-green)"/>
        </linearGradient>
      </defs>
      <polygon points="216,0 432,196 216,391 0,196" fill="url(#tile-blend-back)"/>
    </svg>
    <ul class="contact-list">
      <li>Name</li>
      <li>Address</li>
      <li>Mobile</li>
      <li>Email</li>
    </ul>
  </section>
</main>
</body>
</html>
```